25kg bag for branded milk powder

We are looking for an attractive bag for our Holland dairy milk powder range. We will have 5 kinds of products.

Instant Full Cream milk powder
Full cream milk powder
Instant fat filled milk powder
Skimmed milk powder
Dairy ingredients

The bags are standard industrial 25kg kraft multiply paper bags with inner poly linner.

We want to have an hormonized design where each type of dairy product is differentiated by the product name and a color,

Please see attached design as reference.
Updates

Target Market(s)

Middle East and Africa

Font styles to use
Sans Serif

Requirements
Must have
• The bags must show that we are a dutch company and have a profesional feel.
• We want a general design that will be differentiated by colour coding.
• We want the design to be less conservative compared to the attached examples.
• The bags must be easilly recognisable from all sides as for picture of Corvan Dairies branded bags on pallets attached.
• We have also attached some bags design templates as a reference.
Nice to have
• We would like to use sybols or imagery that symbolises Dutch origin and quality
Should not have
• We cannot have too many images to keep it simple.

```html
<!DOCTYPE html>
<html lang="en">
<head>
<meta charset="utf-8">
<title>Polder Dairy Foods – 25kg milk powder bag range</title>
<link rel="stylesheet" href="https://fonts.googleapis.com/css2?family=Fira+Sans:wght@400;600;700&display=swap">
<style>
  :root {
    --bg: #ececec;
    --bag-white: #fbfbf9;
    --ink: #1e1e1e;
    --yellow: #f0c030;
    --blue: #64c1e4;
    --white: #ffffff;
  }
  * { box-sizing: border-box; margin: 0; padding: 0; }
  html, body { width: 1200px; height: 1200px; overflow: hidden; }
  body {
    background: radial-gradient(circle at 50% 40%, #fafafa 0%, var(--bg) 80%);
    font-family: "Fira Sans", Arial, sans-serif;
    color: var(--ink);
  }
  .range {
    position: absolute; left: 60px; top: 150px;
    display: flex; gap: 30px;
  }
  .bag-face {
    position: relative; width: 340px; height: 900px;
    background: var(--bag-white);
    overflow: hidden;
    box-shadow: 0 10px 30px rgba(0,0,0,.12);
  }
  .bag-face--fat-filled { --accent: var(--yellow); }
  .bag-face--full-cream { --accent: var(--blue); }

  .brand {
    position: absolute; left: 0; right: 0; top: 110px;
    display: flex; align-items: center; justify-content: center; gap: 10px;
  }
  .brand__dot { width: 22px; height: 22px; border-radius: 50%; background: var(--accent); }
  .brand__name { font-size: 24px; font-weight: 600; color: var(--ink); letter-spacing: .5px; }

  .product-name {
    position: absolute; right: 34px; top: 230px;
    text-align: right; color: var(--accent);
    font-weight: 700; font-size: 41px; line-height: 1.08;
  }
  .product-name small {
    display: block; margin-top: 10px;
    font-size: 15px; font-weight: 600;
  }

  .windmill-art {
    position: absolute; left: 40px; top: 470px; width: 170px; height: 250px;
    background: linear-gradient(180deg, transparent 0%, var(--accent) 100%);
    opacity: .55;
  }
  .colour-band { position: absolute; left: 0; bottom: 0; width: 340px; height: 300px; }
  .colour-band path { fill: var(--accent); }
  .net-weight {
    position: absolute; right: 34px; bottom: 110px;
    font-size: 34px; font-weight: 700; line-height: 1; color: var(--white);
  }

  /* back panel */
  .bag-face--back { --accent: var(--blue); }
  .back__title { top: 70px; font-size: 36px; }
  .back__details {
    position: absolute; right: 34px; top: 260px; width: 280px;
    text-align: right; font-size: 14px; font-weight: 600; line-height: 1.35;
  }
  .back__details .brand { position: static; justify-content: flex-end; margin: 12px 0 18px; }
  .back__details .brand__name { font-size: 20px; }
  .back__details p + p { margin-top: 14px; }
  .back__weight { top: 552px; bottom: auto; right: 34px; color: var(--accent); }
  .back .windmill-art { top: 420px; left: 20px; width: 130px; height: 190px; }
  .batch-info {
    position: absolute; left: 24px; bottom: 170px;
    font-size: 13px; font-weight: 600; line-height: 1.9; color: var(--ink);
  }
</style>
</head>
<body>
<main class="range">

  <section class="bag-face bag-face--fat-filled">
    <div class="brand"><span class="brand__dot"></span><span class="brand__name">Polder Dairy Foods</span></div>
    <h2 class="product-name">Instant<br>Fat Filled<br>Milk Powder<small>with Vitamins added</small></h2>
    <div class="windmill-art" role="img" aria-label="Dutch windmill illustration in yellow"></div>
    <svg class="colour-band" viewBox="0 0 340 300" aria-hidden="true">
      <path d="M0 40 C60 22 120 32 170 26 C200 22 215 30 218 48 L218 112 C218 128 236 128 236 112 L236 48 C244 26 292 16 340 30 L340 300 L0 300 Z"/>
    </svg>
    <div class="net-weight">25kg</div>
  </section>

  <section class="bag-face bag-face--full-cream">
    <div class="brand"><span class="brand__dot"></span><span class="brand__name">Polder Dairy Foods</span></div>
    <h2 class="product-name">Instant<br>Full Cream<br>Milk Powder<small>with Vitamins added</small></h2>
    <div class="windmill-art" role="img" aria-label="Dutch windmill illustration in blue"></div>
    <svg class="colour-band" viewBox="0 0 340 300" aria-hidden="true">
      <path d="M0 40 C60 22 120 32 170 26 C200 22 215 30 218 48 L218 112 C218 128 236 128 236 112 L236 48 C244 26 292 16 340 30 L340 300 L0 300 Z"/>
    </svg>
    <div class="net-weight">25kg</div>
  </section>

  <section class="bag-face bag-face--back back">
    <h2 class="product-name back__title">Instant<br>Full Cream<br>Milk Powder<small>with Vitamins added</small></h2>
    <div class="back__details">
      <p>Produced by:</p>
      <div class="brand"><span class="brand__dot"></span><span class="brand__name">Polder Dairy Foods</span></div>
      <p>Molenweg 48<br>Holland<br>Tel: 0297 410 552<br>Fax: 0297 410 553</p>
      <p>Ingredients: Whole cow’s milk</p>
      <p>Registered Factory:<br>R.N.P.N / 21-048190</p>
      <p>Made in Holland</p>
    </div>
    <div class="windmill-art" role="img" aria-label="Dutch windmill illustration in blue"></div>
    <div class="net-weight back__weight">25kg</div>
    <svg class="colour-band" viewBox="0 0 340 300" aria-hidden="true">
      <path d="M0 40 C60 22 120 32 170 26 C200 22 215 30 218 48 L218 112 C218 128 236 128 236 112 L236 48 C244 26 292 16 340 30 L340 300 L0 300 Z"/>
    </svg>
    <div class="batch-info">Date of Production<br>Batch Lot No.</div>
  </section>

</main>
</body>
</html>
```